Postcard Design

I am an attorney and have my own law firm, Law Offices of Gregory T. Halvorsen. My address is 4582 Canterbury Parkway, #318, Glen Burnie, MD 21061. (410) 555-0187. E-mail gthlegal@fernmail.example.

I want to design two full color postcards, I think the size is about 8.5 by 5.5.

The first is attact Driving While Suspended and Driving Without Insurance client's. I have a list of people charged with those crimes and the postcard goes out each week.

I have been sending letters for years and have been successful but am looking to send only postcards. I am very good at writing the message, terrible with art work. I need you to place the information that I provide below onto a post card with the idea that all of those that receive it will call me. Each person charged receives about 5 postcards and 10 letters from lawyers. No other lawyer advertises just Driving While Suspended and Driving Without Insurance, they all advertise DUI/DWI and other types. My goal is for the client to see my postcard and say "I might as well throw the other stuff away because this is the guy who can do my case well for a great price."

Here are the words that I want on the postcard. Some large, some small. Artwork and good coloring a must, that's what I need help with. Need to use both sides and leave only room for address label and stamp.

DRIVING SUSPENDED AND DRIVING WITHOUT INSURANCE $395.00 FLAT FEE.....INCLUDES ALL UNDERLYING CHARGES!

I have have handled over 5000 cases in AA County and Howard County for more than 22 years. I know the Judges, they know me. There is NO reason to spend omre than $395.00 for a first offense driving suspended or driving without insurance. Should you have a lawyer? Yes, nobody should go to court alone. Should you call me? Over 5000 satisfied client's would say so.

MANY CASES DISMISSED BEFORE COURT!

MONEY BACK GUARANTEE......YOU WILL NOT GET POINTS ON YOUR LICENSE FOR YOUR FIRST OFFENSE DRIVING SUSPENDED OR DRIVING WITHOUT INSURANCE. IF YOU DO, I WILL REFUND YOUR ENTIRE FEE!

Law Offices of Gregory T. Halvorsen

Gregory T. Halvorsen, Traffic Defense Attorney

FREE CONSULTATION, PHONES ANSWERED 24/7

HOLLOWAY CREST BUILDING
4582 Canterbury Parkway, #318
Glen Burnie, MD 21061

(410) 555-0187

APPOINTMENTS AVAILABLE DAY, EVENING AND WEEKENDS

Industry/Entity Type

Attorney

Requirements
Must have
• The ad must also include small language on each side of the postcard that says "this is an advertisement"

```html
<!DOCTYPE html>
<html lang="en">
<head>
<meta charset="utf-8">
<title>Postcard Back – Gregory T. Halvorsen, Traffic Defense Attorney</title>
<link rel="stylesheet" href="https://fonts.googleapis.com/css2?family=Tinos:wght@700&family=Open+Sans:wght@400;700&family=Arimo&display=swap">
<style>
  :root {
    --card-cream: #fdf1c9;
    --headline-red: #c01a1a;
    --ink: #111111;
    --rule: #222222;
    --stamp-fill: #ffffff;
  }
  html, body {
    margin: 0;
    padding: 0;
    width: 1200px;
    height: 930px;
    overflow: hidden;
  }
  .postcard-back {
    position: relative;
    width: 1200px;
    height: 930px;
    background: var(--card-cream);
    color: var(--ink);
  }
  .appointments-headline {
    position: absolute;
    left: 34px;
    top: 42px;
    margin: 0;
    font-family: "Tinos", "Times New Roman", serif;
    font-weight: 700;
    font-size: 40px;
    line-height: 49px;
    color: var(--headline-red);
    letter-spacing: 1.1px;
    white-space: nowrap;
  }
  .attorney-block {
    position: absolute;
    left: 33px;
    top: 198px;
    font-family: "Open Sans", "Myriad Pro", sans-serif;
    white-space: nowrap;
  }
  .attorney-name,
  .attorney-title {
    margin: 0;
    font-weight: 700;
    font-size: 26.5px;
    line-height: 36px;
    letter-spacing: -0.5px;
  }
  .office-address {
    margin: 2px 0 0;
    font-style: normal;
    font-size: 26.5px;
    line-height: 45px;
    letter-spacing: -0.5px;
  }
  .office-address span { display: block; }
  .ad-disclaimer {
    position: absolute;
    left: 34px;
    top: 745px;
    margin: 0;
    font-family: "Arimo", Arial, sans-serif;
    font-size: 17px;
    letter-spacing: 1px;
  }
  .stamp-box {
    position: absolute;
    left: 944px;
    top: 74px;
    width: 175px;
    height: 200px;
    background: var(--stamp-fill);
    border: 1.5px solid var(--ink);
  }
  .address-lines {
    position: absolute;
    left: 620px;
    top: 370px;
  }
</style>
</head>
<body>
  <main class="postcard-back">
    <h1 class="appointments-headline">APPOINTMENTS<br>AVAILABLE DAY,<br>EVENING AND WEEKENDS</h1>

    <section class="attorney-block">
      <p class="attorney-name">Gregory T. Halvorsen</p>
      <p class="attorney-title">Traffic Defense Attorney</p>
      <address class="office-address">
        <span>HOLLOWAY CREST BUILDING</span>
        <span>4582 Canterbury Parkway, #318,</span>
        <span>Glen Burnie, MD 21061</span>
        <span>(410) 555-0187</span>
      </address>
    </section>

    <p class="ad-disclaimer">This is an advertisement</p>

    <div class="stamp-box" aria-label="Stamp area"></div>

    <svg class="address-lines" width="506" height="320" viewBox="0 0 506 320" aria-label="Mailing address lines">
      <g stroke="var(--rule)" stroke-width="1.5">
        <line x1="0" y1="9" x2="505" y2="9"/>
        <line x1="0" y1="85" x2="505" y2="85"/>
        <line x1="0" y1="161" x2="505" y2="161"/>
        <line x1="0" y1="237" x2="505" y2="237"/>
        <line x1="0" y1="313" x2="505" y2="313"/>
      </g>
    </svg>
  </main>
</body>
</html>
```